Business Card design for Recruiter providing Recruitment Staff Augmentation services

I need a double sided business card. I have used Plix to print cards in the past and really like their quality. I have a logo but need to change the tagline that is part of the graphic.

The tagline currently reads and Connnecting people with careers - but it should be removed.

The back should look like a notecard for writing a to do list with the first to-do Augment Recruiting Staff

```html
<!DOCTYPE html>
<html lang="en">
<head>
<meta charset="utf-8">
<title>Talent Summit – Business Card</title>
<link href="https://fonts.googleapis.com/css2?family=Open+Sans:wght@400;600;700&display=swap" rel="stylesheet">
<style>
  :root {
    --stage: #2b2b2d;
    --card: #f7f7f7;
    --navy: #1f3f57;
    --accent: #c2452a;
    --ink: #2a2a2a;
    --rule: #1f3f57;
    --note-line: #c9d3dc;
  }
  * { box-sizing: border-box; margin: 0; padding: 0; }
  html, body {
    width: 1200px; height: 997px; overflow: hidden;
    background: var(--stage);
    font-family: "Open Sans", Arial, sans-serif;
  }
  .stage { position: relative; width: 1200px; height: 997px; }
  .card {
    position: absolute; left: 320px;
    width: 560px; height: 320px;
    background: var(--card);
    border-radius: 22px;
    box-shadow: 0 18px 40px rgba(0,0,0,.45);
    overflow: hidden;
  }
  .card--back { top: 90px; }
  .card--front { top: 470px; }

  .brand { display: flex; align-items: center; gap: 12px; }
  .brand__dot { width: 34px; height: 34px; border-radius: 50%; background: var(--accent); flex: none; }
  .brand__name { color: var(--navy); font-weight: 600; letter-spacing: 1px; white-space: nowrap; }

  /* Back: notecard */
  .card--back .brand { position: absolute; left: 40px; top: 30px; }
  .card--back .brand__dot { width: 30px; height: 30px; }
  .card--back .brand__name { font-size: 26px; }

  .todo { position: absolute; left: 40px; right: 40px; top: 92px; list-style: none; }
  .todo li {
    display: flex; align-items: flex-end; gap: 12px;
    height: 42px; padding-bottom: 6px;
    border-bottom: 1px solid var(--note-line);
    color: var(--ink); font-size: 16px;
  }
  .todo__box {
    flex: none; width: 16px; height: 16px; margin-bottom: 3px;
    border: 2px solid var(--accent); border-radius: 3px;
  }

  /* Front */
  .card--front .brand { position: absolute; left: 40px; top: 42px; }
  .card--front .brand__name { font-size: 30px; }

  .rule { position: absolute; height: 2px; background: var(--rule); }
  .rule--top { left: 360px; right: 40px; top: 80px; }
  .rule--name { left: 210px; right: 40px; top: 150px; }

  .holder { position: absolute; left: 40px; top: 128px; }
  .holder__name { color: var(--navy); font-weight: 700; font-size: 20px; line-height: 1.1; }
  .holder__role { color: var(--accent); font-weight: 700; font-size: 11px; letter-spacing: .5px; }

  .web { position: absolute; right: 40px; top: 168px; color: var(--accent); font-weight: 600; font-size: 14px; }

  .contacts { position: absolute; left: 40px; top: 190px; list-style: none; }
  .contacts li {
    display: flex; align-items: flex-start; gap: 10px;
    color: var(--ink); font-size: 14px; line-height: 1.3; margin-bottom: 8px;
  }
  .contacts svg { flex: none; width: 16px; height: 16px; margin-top: 1px; }
</style>
</head>
<body>
<main class="stage">

  <section class="card card--back" aria-label="Card back – to-do notecard">
    <div class="brand">
      <span class="brand__dot"></span>
      <span class="brand__name">TALENT SUMMIT</span>
    </div>
    <ul class="todo">
      <li><span class="todo__box"></span><span>Augment Recruiting Staff</span></li>
      <li><span class="todo__box"></span></li>
      <li><span class="todo__box"></span></li>
      <li><span class="todo__box"></span></li>
      <li><span class="todo__box"></span></li>
    </ul>
  </section>

  <section class="card card--front" aria-label="Card front">
    <div class="brand">
      <span class="brand__dot"></span>
      <span class="brand__name">TALENT SUMMIT</span>
    </div>
    <div class="rule rule--top"></div>

    <div class="holder">
      <p class="holder__name">Dana Whitlock</p>
      <p class="holder__role">FOUNDER &amp; CEO</p>
    </div>
    <div class="rule rule--name"></div>

    <p class="web">www.talentsummit.com</p>

    <ul class="contacts">
      <li>
        <svg viewBox="0 0 16 16" aria-hidden="true"><circle cx="8" cy="8" r="8" fill="var(--accent)"/><path d="M5 6.5c0-.8 1.2-1.2 3-1.2s3 .4 3 1.2v.6H9.6v-.6H6.4v.6H5zM5.5 8h5l.5 3h-6z" fill="#fff"/></svg>
        <span>+1 (555) 014-2286</span>
      </li>
      <li>
        <svg viewBox="0 0 16 16" aria-hidden="true"><circle cx="8" cy="8" r="8" fill="var(--accent)"/><path d="M8 3.8 3.8 7.6h1.2v4h2.2V9.4h1.6v2.2H11v-4h1.2z" fill="#fff"/></svg>
        <span>Unit 42, Block 7, Pune</span>
      </li>
      <li>
        <svg viewBox="0 0 16 16" aria-hidden="true"><circle cx="8" cy="8" r="8" fill="var(--accent)"/><path d="M8 3.5a2.8 2.8 0 0 0-2.8 2.8C5.2 8.4 8 12 8 12s2.8-3.6 2.8-5.7A2.8 2.8 0 0 0 8 3.5zm0 3.8a1 1 0 1 1 0-2 1 1 0 0 1 0 2z" fill="#fff"/></svg>
        <span>18 Maple Row, 2nd Floor,<br>Fairview, CT 06001</span>
      </li>
    </ul>
  </section>

</main>
</body>
</html>
```